Side of Page Partnership-type Letterhead Design for Chiropractic Office

Side oriented letterhead with practice locations/demographics, physician names and company logo

Target Market(s)

Healthcare Professionals & Attorneys

Industry/Entity Type

Healthcare

Font styles to use
Other font styles liked:
• Font of Logo is Trajan Pro, but not a deal breaker if we try something else

Colors

Designer to choose colors to be used in the design.

Requirements
Must have
• All info from attached documents

```html
<!DOCTYPE html>
<html lang="en">
<head>
<meta charset="utf-8">
<title>Northfield Chiropractic Letterhead</title>
<link href="https://fonts.googleapis.com/css2?family=Arimo:wght@400;700&display=swap" rel="stylesheet">
<style>
  :root {
    --backdrop: #d9dadc;
    --paper: #ececec;
    --ink: #5a5b5e;
    --ink-dark: #3b3c40;
    --green: #5a9a34;
    --blue: #233c8f;
  }
  * { margin: 0; padding: 0; box-sizing: border-box; }
  html, body { width: 1200px; height: 1200px; overflow: hidden; background: var(--backdrop); }
  body { font-family: "Arimo", Arial, sans-serif; color: var(--ink); }
  .letterhead {
    position: absolute; left: 196px; top: 30px; width: 807px; height: 1140px;
    background: var(--paper); box-shadow: 0 4px 18px rgba(0,0,0,.18);
  }
  .brand {
    position: absolute; left: 36px; top: 52px; display: flex; align-items: center; gap: 10px;
    font-size: 27px; line-height: 1; color: var(--ink-dark); letter-spacing: .5px;
  }
  .brand-dot { width: 14px; height: 14px; border-radius: 50%; background: var(--green); }
  .divider { position: absolute; left: 214px; top: 178px; width: 1.5px; height: 923px; background: var(--green); }
  .sidebar { position: absolute; left: 36px; font-size: 13.5px; line-height: 16.2px; }
  .physicians { top: 184px; }
  .location { line-height: 16.2px; }
  .loc-riverton { top: 806px; }
  .loc-lakeside { top: 917px; }
  .loc-brookfield { top: 1025px; }
  .contact { display: flex; align-items: center; gap: 5px; }
  .contact svg { width: 9px; height: 9px; fill: var(--blue); }
  .letter { position: absolute; left: 241px; width: 508px; font-size: 13.2px; line-height: 18.9px; }
  .date { top: 183px; }
  .recipient { top: 238px; }
  .recipient strong, .signoff strong { color: var(--ink); font-weight: 700; }
  .greeting { top: 353px; }
  .body { top: 391px; text-align: justify; }
  .body p + p { margin-top: 18.9px; }
  .closing { top: 771px; }
  .signature { position: absolute; left: 232px; top: 800px; width: 290px; height: 28px;
    background: linear-gradient(90deg, rgba(40,40,45,.10), rgba(40,40,45,.04)); border-radius: 3px; }
  .signoff { top: 822px; }
  .footer-band { position: absolute; left: 0; bottom: 0; width: 100%; height: 9px; }
</style>
</head>
<body>
<main class="letterhead">
  <div class="brand"><span class="brand-dot"></span><span>NORTHFIELD CHIROPRACTIC</span></div>

  <div class="sidebar physicians">
    Dana Holloway, DC, DACNB<br>Evan Holloway, DC<br>Grant Whitfield, DC<br>Owen Castellane, DC<br>Miles Durand, DC<br>Luke Pembrook, DC<br>Neil Ashcombe, DC
  </div>

  <div class="sidebar location loc-riverton">
    Riverton<br>4120 Maple Ave.<br>Riverton, OH 43001
    <div class="contact"><svg viewBox="0 0 10 10"><path d="M2 1l2 2-1 1c.5 1.3 1.7 2.5 3 3l1-1 2 2-1.5 1.5C4 9 1 6 .5 2.5z"/></svg>555-010-2100</div>
    <div class="contact"><svg viewBox="0 0 10 10"><rect x="2.5" y="0.5" width="5" height="3"/><rect x="0.5" y="3.5" width="9" height="4" rx="1"/><rect x="2.5" y="7" width="5" height="2.5"/></svg>555-010-2101</div>
  </div>
  <div class="sidebar location loc-lakeside">
    Lakeside<br>218 Harbor St.<br>Lakeside, OH 43002
    <div class="contact"><svg viewBox="0 0 10 10"><path d="M2 1l2 2-1 1c.5 1.3 1.7 2.5 3 3l1-1 2 2-1.5 1.5C4 9 1 6 .5 2.5z"/></svg>555-010-3300</div>
    <div class="contact"><svg viewBox="0 0 10 10"><rect x="2.5" y="0.5" width="5" height="3"/><rect x="0.5" y="3.5" width="9" height="4" rx="1"/><rect x="2.5" y="7" width="5" height="2.5"/></svg>555-010-3301</div>
  </div>
  <div class="sidebar location loc-brookfield">
    Brookfield<br>775 Orchard Rd<br>Brookfield, OH 43003
    <div class="contact"><svg viewBox="0 0 10 10"><path d="M2 1l2 2-1 1c.5 1.3 1.7 2.5 3 3l1-1 2 2-1.5 1.5C4 9 1 6 .5 2.5z"/></svg>555-010-4400</div>
    <div class="contact"><svg viewBox="0 0 10 10"><rect x="2.5" y="0.5" width="5" height="3"/><rect x="0.5" y="3.5" width="9" height="4" rx="1"/><rect x="2.5" y="7" width="5" height="2.5"/></svg>555-010-4401</div>
  </div>

  <div class="divider"></div>

  <div class="letter date">January 1, 2050</div>
  <div class="letter recipient">
    <strong>Jordan Reyes</strong><br>Managing Director<br>Co.Street, Building/Suite<br>City/State, Zip Code
  </div>
  <div class="letter greeting">Dear Alex Morgan,</div>
  <div class="letter body">
    <p>Lorem ipsum dolor sit amet, consectetuer adipiscing elit, sed diam nonummy nibh euismod tincidunt ut laoreet dolore magna aliquam erat volutpat. Ut wisi enim ad minim veniam, quis nostrud exerci tation ullamcorper suscipit lobortis nisl ut aliquip ex ea commodo consequat. Duis dolore te feugait nulla facilisi. Nam liber tempor cum soluta nobis eleifend option congue nihil imperdiet doming id quod mazim placerat facer possim assum.</p>
    <p>Consectetuer adipiscing elit, sed diam nonummy nibh euismod tincidunt ut laoreet dolore magna aliquam erat volutpat. Ut wisi enim ad minim veniam, quis nostrud exerci tation ullamcorper suscipit lobortis nisl ut aliquip ex ea commodo consequat. Consectetuer adipiscing elit, sed diam nonummy nibh euismod tincidunt ut laoreet dolore magna aliquam erat volutpat. Ut wisi enim ad minim veniam, quis nostrud exerci tation ullamcorper suscipit lobortis nisl ut aliquip ex ea commodo consequat.</p>
    <p>Duis dolore te feugait nulla facilisi. Nam liber tempor cum soluta nobis eleifend option congue nihil imperdiet doming id quod mazim placerat facer possim assum.Duis dolore te feugait nulla facilisi. Nam liber tempor cum soluta nobis eleifend option congue nihil imperdiet doming id quod mazim placerat facer possim assum.</p>
  </div>
  <div class="letter closing">Sincerely Yours,</div>
  <div class="signature" role="img" aria-label="Handwritten signature of the managing director"></div>
  <div class="letter signoff"><strong>Authorized Managing Director</strong><br>Your Company Name</div>

  <svg class="footer-band" viewBox="0 0 807 9" preserveAspectRatio="none">
    <polygon points="0,0 218,0 209,9 0,9" fill="var(--blue)"/>
    <polygon points="222,0 807,0 807,9 213,9" fill="var(--green)"/>
  </svg>
</main>
</body>
</html>
```